Brookmere Osteopathy flyer

I want a clean clear DL flyer (but also want an A4 poster) promoting a new Osteopathic business in a semi rural area in Tasmania (Australia).
It can have pictures like the examples attached to show people what Osteopathy is (its like Chiropractic and physiotherapy).
I am the sole practioner and am male, so any pictures would be best to be a white male if possible.
I've attached some wording, you can use all, or none of it
I don't have a phone number for the business yet
info@brookmereosteopathy.example
www.brookmereosteopathy.example
Target Market(s)
Australians, from tradies, professionals, babies to retired people
Industry/Entity Type
Health
Look and feel

```html
<!DOCTYPE html>
<html lang="en">
<head>
<meta charset="utf-8">
<title>Brookmere Osteopathy – DL flyer</title>
<link href="https://fonts.googleapis.com/css2?family=Arimo:wght@400;700&family=Roboto+Condensed:wght@700&display=swap" rel="stylesheet">
<style>
  :root{
    --page:#f2f2f2;
    --blue-light:#1f9ad6;
    --blue-mid:#136da3;
    --blue-dark:#0a4870;
    --white:#ffffff;
    --ink:#111111;
    --skin:#e8b79a;
    --skin-deep:#d99a78;
    --room:#e9ecef;
    --accent:#1e8fcc;
  }
  *{box-sizing:border-box;margin:0;padding:0}
  html,body{width:1200px;height:960px;overflow:hidden;background:var(--page)}
  body{position:relative;font-family:"Arimo",Arial,sans-serif}
  .flyer{
    position:absolute;top:50px;width:404px;height:856px;overflow:hidden;
    background:linear-gradient(180deg,var(--blue-light) 0%,var(--blue-light) 38%,var(--blue-mid) 70%,var(--blue-dark) 100%);
  }
  .flyer--front{left:178px}
  .flyer--back{left:617px}
  .flyer__art{position:absolute;inset:0;width:404px;height:856px}
  .logo-badge{
    position:absolute;left:238px;top:356px;width:140px;height:140px;border-radius:50%;
    background:var(--white);display:flex;align-items:center;justify-content:center;text-align:center;
    border:4px solid var(--white);
  }
  .logo-badge__name{font-family:"Arimo",Arial,sans-serif;font-weight:400;font-size:15px;line-height:1.25;color:var(--accent);width:100px}
  .reasons{position:absolute;left:35px;top:494px;color:var(--white)}
  .reasons__title{font-family:"Roboto Condensed","Arial Narrow",sans-serif;font-weight:700;font-size:27px;line-height:36px}
  .reasons__list{list-style:none;margin-top:10px}
  .reasons__list li{font-size:17px;line-height:20.8px;padding-left:20px;position:relative}
  .reasons__list li::before{content:"";position:absolute;left:2px;top:7px;width:6px;height:6px;background:var(--white);transform:rotate(45deg)}
  .web-band{
    position:absolute;left:0;top:782px;width:404px;height:39px;background:var(--white);
    display:flex;align-items:center;justify-content:center;
    font-weight:700;font-size:19px;color:var(--ink);
  }
  .about{
    position:absolute;left:31px;top:552px;width:342px;color:var(--white);
    font-size:16px;line-height:20.5px;text-align:justify;
  }
  .divider{position:absolute;left:45px;top:657px;width:314px;height:2px;background:var(--white);border-radius:2px}
  .contact{position:absolute;left:31px;top:693px;list-style:none;color:var(--white)}
  .contact li{display:flex;align-items:center;gap:12px;height:26px;font-size:16.5px}
  .contact li.contact__phone{font-weight:700;font-size:20px}
  .contact svg{width:17px;height:17px;flex:none}
</style>
</head>
<body>

<section class="flyer flyer--front" aria-label="Flyer front">
  <svg class="flyer__art" viewBox="0 0 404 856" aria-hidden="false">
    <defs>
      <linearGradient id="backPhotoTone" x1="0" y1="0" x2="1" y2="1">
        <stop offset="0" stop-color="#f3d2bf"/>
        <stop offset="0.55" stop-color="var(--skin)"/>
        <stop offset="1" stop-color="#f4f4f4"/>
      </linearGradient>
      <linearGradient id="treatPhotoTone" x1="0" y1="0" x2="0" y2="1">
        <stop offset="0" stop-color="#f0f0f0"/>
        <stop offset="0.6" stop-color="#e6d3c6"/>
        <stop offset="1" stop-color="#c9b3a5"/>
      </linearGradient>
    </defs>
    <path role="img" aria-label="Photo: practitioner's hands treating a patient's shoulder and spine"
          d="M0 0 H404 V206 Q250 380 0 262 Z" fill="url(#backPhotoTone)" stroke="var(--white)" stroke-width="6"/>
    <circle role="img" aria-label="Photo: osteopath gently treating a patient's neck on a treatment table"
            cx="126" cy="358" r="109" fill="url(#treatPhotoTone)" stroke="var(--white)" stroke-width="7"/>
  </svg>

  <div class="logo-badge"><span class="logo-badge__name">Brookmere Osteopathy</span></div>

  <div class="reasons">
    <h2 class="reasons__title">Common reasons<br>people visit an osteopath:</h2>
    <ul class="reasons__list">
      <li>Back / neck pain</li>
      <li>Headaches / migraines</li>
      <li>Joint and muscle pain</li>
      <li>Pregnancy-related discomfort</li>
      <li>Disc related issues</li>
      <li>Sciatica</li>
      <li>Plantar fasciitis</li>
      <li>Tendonitis / Bursitis</li>
      <li>Adhesive capsulitis (frozen shoulder)</li>
      <li>Tennis / Golfers elbow</li>
    </ul>
  </div>

  <div class="web-band">www.brookmereosteopathy.example</div>
</section>

<section class="flyer flyer--back" aria-label="Flyer back">
  <svg class="flyer__art" viewBox="0 0 404 856">
    <defs>
      <linearGradient id="upperBackTone" x1="0" y1="0" x2="1" y2="1">
        <stop offset="0" stop-color="#e4e6e8"/>
        <stop offset="0.35" stop-color="var(--skin)"/>
        <stop offset="1" stop-color="var(--skin-deep)"/>
      </linearGradient>
      <linearGradient id="shoulderTone" x1="0" y1="0" x2="1" y2="1">
        <stop offset="0" stop-color="#f1f1f1"/>
        <stop offset="0.6" stop-color="#e2b89f"/>
        <stop offset="1" stop-color="#f7f7f7"/>
      </linearGradient>
      <linearGradient id="treatPhotoToneBack" x1="0" y1="0" x2="0" y2="1">
        <stop offset="0" stop-color="#f0f0f0"/>
        <stop offset="0.6" stop-color="#e6d3c6"/>
        <stop offset="1" stop-color="#c9b3a5"/>
      </linearGradient>
    </defs>
    <path role="img" aria-label="Photo: practitioner's hand assessing a man's upper back"
          d="M0 0 H404 V200 Q330 430 0 410 Z" fill="url(#upperBackTone)" stroke="var(--white)" stroke-width="6"/>
    <circle role="img" aria-label="Photo: practitioner mobilising a patient's shoulder"
            cx="311" cy="94" r="116" fill="url(#shoulderTone)" stroke="var(--white)" stroke-width="7"/>
    <circle role="img" aria-label="Photo: osteopath gently treating a patient's neck on a treatment table"
            cx="274" cy="382" r="109" fill="url(#treatPhotoToneBack)" stroke="var(--white)" stroke-width="7"/>
  </svg>

  <p class="about">Osteopaths use a combination of joint manipulation, targeted deep tissue massage and stretching to improve function, relieve pain and support the body’s ability to heal itself</p>

  <div class="divider"></div>

  <ul class="contact">
    <li>
      <svg viewBox="0 0 17 17" aria-hidden="true"><rect width="17" height="17" rx="3" fill="var(--white)"/><path d="M8.5 3.2a3.4 3.4 0 0 0-3.4 3.4c0 2.6 3.4 6.8 3.4 6.8s3.4-4.2 3.4-6.8a3.4 3.4 0 0 0-3.4-3.4zm0 4.8a1.4 1.4 0 1 1 0-2.8 1.4 1.4 0 0 1 0 2.8z" fill="var(--blue-mid)"/></svg>
      48 Mill Creek Road, Brookmere
    </li>
    <li class="contact__phone">
      <svg viewBox="0 0 17 17" aria-hidden="true"><rect width="17" height="17" rx="3" fill="var(--white)"/><path d="M5.4 3.5l1.8 2.4-1 1.2c.7 1.5 1.8 2.6 3.2 3.3l1.2-1 2.4 1.8-.8 2c-4.3-.3-7.5-3.5-7.9-7.9z" fill="var(--blue-mid)"/></svg>
      000 000 0000
    </li>
    <li>
      <svg viewBox="0 0 17 17" aria-hidden="true"><rect width="17" height="17" rx="3" fill="var(--white)"/><rect x="3.5" y="5" width="10" height="7.5" rx="1" fill="none" stroke="var(--blue-mid)" stroke-width="1.4"/><path d="M3.8 5.5l4.7 3.7 4.7-3.7" fill="none" stroke="var(--blue-mid)" stroke-width="1.4"/></svg>
      info@brookmereosteopathy.example
    </li>
  </ul>

  <div class="web-band">www.brookmereosteopathy.example</div>
</section>

</body>
</html>
```